Morvela Aesthetic Doctor

I require an elegant, luxurious looking business card for my aesthetic business. I am a doctor and that will set me aside from competitors. I am planning to provide home and spa based treatments to clients with high expectations. I have attached my logo.

```html
<!DOCTYPE html>
<html lang="en">
<head>
<meta charset="utf-8">
<title>Morvela Aesthetic Doctor – Business Card</title>
<link rel="stylesheet" href="https://fonts.googleapis.com/css2?family=Open+Sans:wght@300;400;600&display=swap">
<style>
  :root{
    --page:#ece9e4;
    --card-white:#ffffff;
    --card-white-edge:#eeeeee;
    --brand-blue:#1f6fbf;
    --accent-blue:#29a3e0;
    --text-grey:#8a8a8a;
    --mark-grey:#a3a3a3;
    --back-blue-top:#2484cc;
    --back-blue-bottom:#1462ad;
    --pill-blue:#8ccdee;
    --white:#ffffff;
  }
  *{box-sizing:border-box;margin:0;padding:0}
  html,body{width:1200px;height:1136px;overflow:hidden}
  body{
    background:var(--page);
    font-family:"Open Sans",Arial,sans-serif;
    position:relative;
  }
  .card{
    position:absolute;left:160px;width:880px;height:503px;
    border-radius:4px;overflow:hidden;
    box-shadow:0 10px 30px rgba(0,0,0,.18);
  }
  .card--front{top:43px;background:radial-gradient(ellipse at 55% 35%,var(--card-white) 40%,var(--card-white-edge) 100%)}
  .card--back{top:590px;background:linear-gradient(160deg,var(--back-blue-top),var(--back-blue-bottom))}

  /* brand lockup */
  .brand{position:absolute;display:flex;align-items:center;gap:22px}
  .brand__ring{border-radius:50%;border:3px solid currentColor;flex:none}
  .brand__name{font-weight:300;line-height:1;text-transform:uppercase}
  .brand__name span{display:block}
  .brand--front{left:56px;top:98px;color:var(--mark-grey)}
  .brand--front .brand__ring{width:108px;height:108px}
  .brand--front .brand__title{font-size:62px;letter-spacing:7px}
  .brand--front .brand__sub{font-size:25px;letter-spacing:3px;margin-top:8px}
  .brand--back{left:150px;top:120px;color:var(--white)}
  .brand--back .brand__ring{width:128px;height:128px}
  .brand--back .brand__title{font-size:74px;letter-spacing:8px}
  .brand--back .brand__sub{font-size:29px;letter-spacing:3px;margin-top:10px}

  /* front: person */
  .person{position:absolute;left:186px;top:262px}
  .person__name{font-size:31px;color:var(--brand-blue);font-weight:400}
  .person__creds{font-size:14px;color:var(--accent-blue);margin-left:6px;letter-spacing:.5px}
  .person__role{font-size:19px;color:var(--text-grey);margin-top:4px}
  .person__rule{width:42px;height:3px;background:var(--accent-blue);margin:18px 0 16px}
  .contact{list-style:none}
  .contact li{display:flex;align-items:center;gap:14px;font-size:18px;color:var(--text-grey);line-height:31px}
  .contact svg{width:16px;height:16px;fill:var(--accent-blue);flex:none}

  /* front: services */
  .services{position:absolute;right:56px;top:52px;list-style:none;text-align:right}
  .services li{font-size:19px;color:var(--text-grey);line-height:36px;display:flex;justify-content:flex-end;align-items:center;gap:16px}
  .services li::after{content:"";width:8px;height:8px;border-radius:50%;background:var(--accent-blue)}
  .social{position:absolute;right:52px;top:246px;display:flex;gap:10px}
  .social span{width:20px;height:20px;border-radius:50%;background:var(--accent-blue)}

  /* back */
  .offer{position:absolute;left:0;right:0;top:300px;text-align:center;color:var(--white);font-size:21px;line-height:32px;font-weight:400}
  .pill{
    position:absolute;left:50%;top:400px;transform:translateX(-50%);
    background:var(--pill-blue);color:var(--white);
    font-size:25px;padding:10px 44px;border-radius:30px;white-space:nowrap;
  }
</style>
</head>
<body>
  <section class="card card--front" aria-label="Business card front">
    <div class="brand brand--front">
      <span class="brand__ring" aria-hidden="true"></span>
      <p class="brand__name"><span class="brand__title">Morvela</span><span class="brand__sub">Aesthetic Doctor</span></p>
    </div>

    <div class="person">
      <p class="person__name">Dr Elise Varnham<span class="person__creds">MRCPCH MD</span></p>
      <p class="person__role">Australasian Diploma of Aesthetic Medicine</p>
      <div class="person__rule"></div>
      <ul class="contact">
        <li><svg viewBox="0 0 16 16" aria-hidden="true"><path d="M3.5 1.5l2.5 3-1.5 1.8c.9 2 2.4 3.5 4.2 4.3l1.8-1.5 3 2.5-1.2 2.4C7.6 13.9 2.1 8.4 1.1 2.7z"/></svg>0800 555 014</li>
        <li><svg viewBox="0 0 16 16" aria-hidden="true"><path d="M1 3h14v10H1zM1.8 3.8L8 8.6l6.2-4.8" stroke="#fff" stroke-width="1"/></svg>elise@morvela.co.nz</li>
        <li><svg viewBox="0 0 16 16" aria-hidden="true"><circle cx="8" cy="8" r="7"/><path d="M1 8h14M8 1c-3 3-3 11 0 14M8 1c3 3 3 11 0 14" stroke="#fff" stroke-width="1" fill="none"/></svg>www.morvela.co.nz</li>
      </ul>
    </div>

    <ul class="services">
      <li>Dermal injectables</li>
      <li>Plasma facials</li>
      <li>Microneedling</li>
      <li>Skin boosters</li>
      <li>Excessive sweating</li>
    </ul>
    <div class="social" aria-label="Social media"><span></span><span></span></div>
  </section>

  <section class="card card--back" aria-label="Business card back">
    <div class="brand brand--back">
      <span class="brand__ring" aria-hidden="true"></span>
      <p class="brand__name"><span class="brand__title">Morvela</span><span class="brand__sub">Aesthetic Doctor</span></p>
    </div>
    <p class="offer">Dermal injectables - Plasma facials - Microneedling<br>Skin boosters - Excessive sweating</p>
    <p class="pill">Home and Spa Based Treatments</p>
  </section>
</body>
</html>
```